Simple+Professional tech feel + warm and friendly box design for pet test kit

Project Name: 10-Minute Canine & Feline Rapid Test Kit Packaging Design
Target Brand Reference: VETRALUX (South Korea) styles
Design Style Direction: Professional tech feel + warm and friendly
Professionalism (Professional): Clear typography and distinct information hierarchy to reflect the product’s scientific rigor and accuracy.
Technological: Reflected through clean graphics and a minimalist layout.
Friendly: Utilise soft, warm colour combinations to convey care for pets and well-wishes for their health.
International: The design should align with mainstream aesthetics and avoid cultural ambiguities.

Target Market(s)
European Union and the United States
Industry/Entity Type
Veterinary Medical
Look and feel
Each slider illustrates characteristics of the customer's brand and the style your logo design should communicate.

```html
<!DOCTYPE html>
<html lang="en">
<head>
<meta charset="utf-8">
<title>PawLume Rapid Test Kit Packaging</title>
<link href="https://fonts.googleapis.com/css2?family=Montserrat:wght@400;500;600;700&display=swap" rel="stylesheet">
<style>
  :root{
    --bg:#e4e5e5;
    --panel:#f7f7f6;
    --green:#6cb52d;
    --green-dark:#4c9a1f;
    --green-light:#b5d96e;
    --ink:#2a2a2a;
    --muted:#4a4a4a;
  }
  *{box-sizing:border-box;margin:0;padding:0}
  html,body{width:1200px;height:912px;overflow:hidden}
  body{background:var(--bg);font-family:"Montserrat",sans-serif;color:var(--ink);position:relative}
  .panel{position:absolute;background:var(--panel);overflow:hidden}
  .wave-band{position:absolute;left:0;width:100%;background:linear-gradient(90deg,var(--green) 0%,var(--green-light) 100%)}
  .lid{left:401px;top:248px;width:335px;height:164px;background:var(--green);display:flex;align-items:center;justify-content:center}
  .wordmark{font-weight:700;color:var(--ink);letter-spacing:-0.5px;line-height:1;white-space:nowrap}
  .lid .wordmark{font-size:38px}

  .front{left:45px;top:474px;width:353px;height:227px}
  .front .wordmark{position:absolute;left:20px;top:20px;font-size:30px}
  .tests-tag{position:absolute;left:237px;top:22px;width:103px;height:20px;background:var(--green);color:#fff;font-size:11px;line-height:20px;padding-left:7px}
  .subtitle{position:absolute;left:20px;top:59px;font-size:10px;line-height:11px;color:var(--ink)}
  .subtitle b{font-weight:700}
  .pet-art{position:absolute;left:30px;top:98px;width:72px;height:50px;border-radius:10px;background:linear-gradient(160deg,#e9f3dc,#cfe6ae)}
  .front .wave-band{top:154px;height:28px}
  .maker{position:absolute;display:flex;align-items:center;gap:6px;font-weight:700;color:var(--ink);white-space:nowrap}
  .maker .dot{width:10px;height:10px;border-radius:50%;background:var(--green)}
  .front .maker{left:200px;top:192px;font-size:17px}

  .side{left:405px;top:474px;width:162px;height:227px}
  .side .notice{position:absolute;left:8px;right:8px;top:33px;text-align:center;font-size:9px;font-weight:600;line-height:10px}
  .side .info{position:absolute;left:13px;top:80px;font-size:8px;line-height:9.2px;color:var(--muted)}
  .side .info b{color:var(--ink)}
  .side .wave-band{top:134px;height:30px}
  .symbols{position:absolute;left:12px;top:180px;display:flex;align-items:center;gap:7px;color:var(--green)}
  .symbols svg{display:block}
  .sym-box{border:1.2px solid var(--green);padding:1px 3px;font-size:8px;line-height:10px}
  .temp{display:flex;align-items:flex-end;gap:2px;font-size:6.5px;line-height:7px}
  .temp .hi{align-self:flex-start}

  .back{left:600px;top:474px;width:338px;height:227px}
  .back .wordmark{position:absolute;left:22px;top:20px;font-size:30px}
  .back .wave-band{top:128px;height:36px}
  .back .maker{left:205px;top:180px;font-size:17px}
  .back .tests-label{position:absolute;left:30px;top:200px;color:var(--green);font-size:11px;font-weight:500}

  .side2{left:943px;top:474px;width:171px;height:227px}
  .story{position:absolute;left:33px;top:22px;width:120px;font-size:7.6px;line-height:9px;color:var(--muted)}
  .story b{color:var(--ink)}
  .side2 .wave-band{top:130px;height:34px}
  .side2 .wordmark{position:absolute;left:36px;top:184px;font-size:19px}
</style>
</head>
<body>
  <div class="panel lid"><span class="wordmark">PawLume</span></div>

  <section class="panel front">
    <div class="wordmark">PawLume</div>
    <div class="tests-tag">5 Tests Kit</div>
    <p class="subtitle"><b>10-Minute</b> Canine &amp; Feline<br><b>Rapid Test Kit</b><br>For Dogs and Cat</p>
    <div class="pet-art" role="img" aria-label="Line illustration of a dog and a cat sitting together"></div>
    <div class="wave-band" role="img" aria-label="Layered green wave decoration"></div>
    <div class="maker"><span class="dot"></span>KELDRIN</div>
  </section>

  <section class="panel side">
    <p class="notice">(For accurate results, please read the instructions carefully before use)</p>
    <p class="info">A Clear View into Pet Health<br>Made by Keldrin<br>Keldrin Biotech Limited<br>Web:<b>www.keldrin.com</b><br>E-mail:sales@keldrin.com</p>
    <div class="wave-band" role="img" aria-label="Layered green wave decoration"></div>
    <div class="symbols" aria-label="Storage and use symbols">
      <svg width="15" height="15" viewBox="0 0 15 15"><circle cx="7.5" cy="7.5" r="6.5" fill="none" stroke="var(--green)" stroke-width="1.3"/><text x="7.5" y="10.5" font-size="9" font-weight="600" text-anchor="middle" fill="var(--green)" font-family="Montserrat,sans-serif">2</text><line x1="3" y1="12" x2="12" y2="3" stroke="var(--green)" stroke-width="1"/></svg>
      <svg width="15" height="15" viewBox="0 0 15 15"><path d="M1.5,7 A6,6 0 0 1 13.5,7 Z" fill="var(--green)"/><path d="M7.5,7 V12.5 A1.3,1.3 0 0 1 5,12.5" fill="none" stroke="var(--green)" stroke-width="1.2"/></svg>
      <svg width="15" height="15" viewBox="0 0 15 15"><circle cx="7.5" cy="7.5" r="3" fill="none" stroke="var(--green)" stroke-width="1.2"/><g stroke="var(--green)" stroke-width="1.1"><line x1="7.5" y1="0.5" x2="7.5" y2="3"/><line x1="7.5" y1="12" x2="7.5" y2="14.5"/><line x1="0.5" y1="7.5" x2="3" y2="7.5"/><line x1="12" y1="7.5" x2="14.5" y2="7.5"/><line x1="2.5" y1="2.5" x2="12.5" y2="12.5"/></g></svg>
      <span class="sym-box">IVD</span>
      <span class="temp"><span>4°C</span><svg width="6" height="16" viewBox="0 0 6 16"><line x1="3" y1="1" x2="3" y2="12" stroke="var(--green)" stroke-width="1.4"/><circle cx="3" cy="13" r="2.3" fill="var(--green)"/></svg><span class="hi">30°C</span></span>
    </div>
  </section>

  <section class="panel back">
    <div class="wordmark">PawLume</div>
    <div class="wave-band" role="img" aria-label="Layered green wave decoration"></div>
    <div class="maker"><span class="dot"></span>KELDRIN</div>
    <div class="tests-label">5 Tests Kit</div>
  </section>

  <section class="panel side2">
    <p class="story">"<b>PawLume</b> is made by Keldrin, our name combines 'Kel' for keen science with "Drin" for care, representing both intelligent efficacy in our testing and deep respect for the life of every animal we serve</p>
    <div class="wave-band" role="img" aria-label="Layered green wave decoration"></div>
    <div class="wordmark">PawLume</div>
  </section>
</body>
</html>
```